Private Dining Restaurant Menu Design

Looking for help in designing a private dining room menu brochure - probably would need 4 panel layout to make all of the content fit, or a 5.5x8" booklet. Open to your ideas on layout/vessel - would want to post on website and be able to print to hand out to guests interested in booking our private dining room.

All content is in the attached "Private Dining Menu".

Would like to match existing dinner menu design - also attached.

Website is www.copperfernkitchen.com

Requirements
Must have
• Easy to read format of a brochure of the private dining menu content - want to be able to hand out to interested guests and have it simple and easy to read/flip through.

```html
<!DOCTYPE html>
<html lang="en">
<head>
<meta charset="utf-8">
<title>Dinner Options – Copper Fern Kitchen</title>
<link href="https://fonts.googleapis.com/css2?family=Merriweather:wght@700&family=Roboto:ital,wght@0,400;0,700;1,400&display=swap" rel="stylesheet">
<style>
  :root {
    --navy: #1b2b5c;
    --panel-navy: #263d6e;
    --linen: #eceadf;
    --tan: #ddd3c2;
    --paper: #ffffff;
    --wine: #8c2a2a;
    --ink: #1e2233;
    --item-navy: #1f2f63;
    --scene-top: #e9e6d8;
    --scene-bottom: #7c7460;
  }
  * { box-sizing: border-box; margin: 0; padding: 0; }
  html, body { width: 825px; height: 1200px; overflow: hidden; background: var(--navy); }
  .menu-page {
    position: relative; width: 825px; height: 1200px;
    border: 10px solid var(--navy); background: var(--paper); overflow: hidden;
    font-family: "Roboto", Arial, sans-serif;
  }
  .forest-header {
    position: absolute; left: 0; top: 0; width: 805px; height: 245px;
    background: linear-gradient(180deg, var(--scene-top) 0%, #c9c3ae 40%, var(--scene-bottom) 100%);
  }
  .linen-band {
    position: absolute; left: 0; top: 245px; width: 805px; height: 420px;
    background: var(--linen);
  }
  .tan-band {
    position: absolute; left: 0; top: 665px; width: 805px; height: 233px;
    background: var(--tan);
  }
  .title-panel {
    position: absolute; left: 118px; top: 176px; width: 565px; height: 134px;
    background: var(--panel-navy); border-radius: 12px;
    box-shadow: 0 3px 8px rgba(0,0,0,.3);
    text-align: center; color: #fff;
  }
  .title-panel h1 {
    font-family: "Merriweather", Georgia, serif; font-weight: 700;
    font-size: 31px; letter-spacing: .5px; margin-top: 30px;
  }
  .title-panel p { font-size: 14px; margin-top: 19px; color: #e8e8ee; }
  .prep-note {
    position: absolute; left: 50px; top: 348px; width: 705px;
    text-align: center; font-size: 16px; line-height: 23px; color: var(--ink);
  }
  .option { position: absolute; top: 420px; width: 330px; }
  .option--a { left: 50px; }
  .option--b { left: 430px; }
  .option h2 {
    font-family: "Merriweather", Georgia, serif; font-weight: 700;
    font-size: 21px; color: var(--wine);
  }
  .option h2 small { font-size: 16px; }
  .option .sides {
    margin: 10px 0 0 24px; width: 298px; text-align: justify;
    font-style: italic; font-size: 12.5px; line-height: 15px; color: var(--wine);
  }
  .option ul { list-style: none; margin: 17px 0 0 24px; }
  .option li {
    font-weight: 700; font-size: 13px; line-height: 22.7px; color: var(--item-navy);
  }
  .room-card {
    position: absolute; left: 179px; top: 685px; width: 442px; height: 475px;
    background: var(--panel-navy); border-radius: 12px;
    box-shadow: 0 3px 8px rgba(0,0,0,.3);
  }
  .room-photo {
    position: absolute; left: 9px; top: 31px; width: 425px; height: 319px;
    background: linear-gradient(180deg, #7d7a74 0%, #4a4038 45%, #2a2420 100%);
  }
</style>
</head>
<body>
<main class="menu-page">
  <div class="forest-header" role="img" aria-label="Misty mountain forest landscape with pine trees and birds in flight"></div>
  <div class="linen-band"></div>
  <div class="tan-band"></div>

  <header class="title-panel">
    <h1>DINNER OPTIONS</h1>
    <p>an option below must be chosen for groups of 15 or more, served after 3pm</p>
  </header>

  <p class="prep-note">*It is greatly appreciated if you are able to give pre-determined individual menu orders to help with food prep and operations of the event</p>

  <section class="option option--a">
    <h2>Option A - $20<small>/Person</small></h2>
    <p class="sides">Served with bacon &amp; scallion mashed potatoes and steamed broccoli Also includes choice of starter house or Caesar salad</p>
    <ul>
      <li>½ Copper Fern's Famous Wood-Roasted Chicken</li>
      <li>½ Slab Sweet &amp; Smoky BBQ Baby Back Ribs</li>
      <li>6 oz Fresh Norwegian Salmon</li>
      <li>6 oz Wood-Grilled Sirloin</li>
    </ul>
  </section>

  <section class="option option--b">
    <h2>Option B - $27<small>/Person</small></h2>
    <p class="sides">Served with bacon &amp; scallion mashed potatoes and steamed broccoli Also includes choice of starter house or Caesar salad</p>
    <ul>
      <li>30-Day Aged Wood-Grilled Ribeye – 14 oz</li>
      <li>6 oz Wood-Grilled Sirloin &amp; Grilled Shrimp</li>
      <li>½ Slab BBQ Ribs &amp; ¼ Wood-Roasted Chicken</li>
      <li>Full Rack of BBQ Baby Back Ribs</li>
    </ul>
  </section>

  <figure class="room-card">
    <div class="room-photo" role="img" aria-label="Private dining room with round tables set with white linens, stone fireplace and tall windows"></div>
  </figure>
</main>
</body>
</html>
```